Web Design Project

I need a three page website. I have designed the index.html and the specialevent.html page.

I need someone to finetune the pages for me.

Where I have difficulty is with the following:
I want to add an event table driven by php database.
The administrator of the event will login and create the wording that fits under each colmn. The administrator the submit the form to php database. The database then display in a html.

The Table contains 5 coloums and the rows can vary and can go up to as many as 100.

The table set out events on a program
In the last column of every row I need a submit button to "View and Book" I need to link those buttons with external links/pages.

I use Dreamweaver CS5 and I need to have it in this format in order for me to edit it in the future.

The Table needs to be updated once a year for this program. So ideally if someone has a password to update the certain regions this is what I have in mind.

I have also designed a mockup of the restaurant page. At the top I need.
1) 4 Colapsable panels
a) Restaurants - opening the names of the restaurants
b) Coffee shops and light lunches .... with the names
c) Family
d) Home eateries

From the colapsable panel of each of these I need a anchored link to the description/photos of each...with a BOOK now button I can submit bookings to.

I added a colapsable panel in each restaurants description to keep everything contained.

Please help

• Background must be fixed so that main.div scroll over it

The colours are chosen so please stick to it.

The green for the submit button I short is. #C8D707

I need to edit the pages in Dreamweaver CS5. /Flexilayout2pro

Please ask if you need to know anything. I exactly know what I want.

Kind regards
Marius Delport

The colours are fine.

The wording " lindekloofdirect BOOKING agent" should appear right at the top in the white horizon part of the background image.

The specialevent page I described already. I am interested in the editable solution. for this.

I will make up a mockup of the third page and send it later.

Regards

```html
<!DOCTYPE html>
<html lang="en">
<head>
<meta charset="utf-8">
<title>Lindekloof Direct – Booking Agent</title>
<link rel="stylesheet" href="https://fonts.googleapis.com/css2?family=Asap:wght@400;500;600;700&display=swap">
<style>
  :root {
    --page-bg: #666666;
    --lime: #c8d707;
    --lime-dark: #8a9312;
    --white: #ffffff;
    --ink: #333333;
    --muted: #a6a6a6;
    --icon-grey: #b3b3b3;
    --stay: #ff6633;
    --play: #ffff99;
    --play-word: #a8b817;
    --eat: #5bc8f2;
    --date-chip: #444444;
    --rule: #cccccc;
  }
  * { box-sizing: border-box; margin: 0; padding: 0; }
  html, body {
    width: 1129px; height: 1200px; overflow: hidden;
    background: var(--page-bg);
    font-family: "Asap", Arial, sans-serif;
    color: var(--white);
  }
  .page { position: relative; width: 932px; margin: 0 auto; left: 1px; }

  .site-header { height: 126px; position: relative; }
  .brand {
    position: absolute; left: 0; top: 46px;
    font-size: 35px; font-weight: 500; color: var(--lime); letter-spacing: 0.2px;
  }
  .social { position: absolute; right: 0; top: 50px; display: flex; gap: 7px; }
  .social span { width: 31px; height: 31px; border-radius: 50%; background: var(--icon-grey); display: block; }

  .main-nav {
    height: 69px; background: var(--lime); border-radius: 7px;
    display: flex; align-items: center;
  }
  .main-nav a {
    display: block; height: 69px; line-height: 69px; padding: 0 40px;
    color: var(--white); text-decoration: none; font-weight: 600; font-size: 17px;
    border-right: 1px solid rgba(255,255,255,0.25);
  }
  .main-nav a:last-child { border-right: none; }
  .main-nav a.active { color: #111; padding: 0 40px 0 46px; }

  .tagline { margin-top: 36px; font-size: 30px; font-weight: 400; color: var(--muted); }

  .services { margin-top: 24px; display: flex; }
  .service { text-align: center; }
  .service--stay { width: 293px; }
  .service--play { width: 344px; }
  .service--eat { width: 295px; }
  .service-title { height: 72px; line-height: 72px; font-size: 28px; font-weight: 700; }
  .service--stay .service-title { background: var(--stay); color: var(--white); border-top-left-radius: 7px; }
  .service--play .service-title { background: var(--play); color: var(--play-word); }
  .service--eat .service-title { background: var(--eat); color: var(--white); border-top-right-radius: 7px; }
  .service-photo { height: 189px; }
  .service--stay .service-photo { background: linear-gradient(160deg, #d89a3e 0%, #b7742b 45%, #efe6dc 75%, #a86a2f 100%); border-bottom-left-radius: 7px; }
  .service--play .service-photo { background: radial-gradient(circle at 55% 30%, #f3b35a 0%, #b8561e 35%, #3a1608 75%, #150804 100%); }
  .service--eat .service-photo { background: linear-gradient(135deg, #c33a2a 0%, #8a3a1c 35%, #c98a3a 65%, #6d8b2e 100%); border-bottom-right-radius: 7px; }
  .service-text { padding: 20px 22px 0; font-size: 15.8px; line-height: 22.6px; color: var(--white); }
  .service--play .service-text { padding: 20px 40px 0; }

  .events {
    margin-top: 28px; height: 259px; background: var(--white); border-radius: 7px;
    padding: 24px 40px 0 25px; color: var(--ink);
  }
  .events h2 { font-size: 18px; font-weight: 500; margin-bottom: 28px; }
  .event { display: flex; gap: 12px; }
  .event + .event { margin-top: 18px; }
  .event-date {
    flex: none; width: 37px; height: 37px; border-radius: 4px; background: var(--date-chip);
    color: var(--white); font-size: 12px; line-height: 14px; text-align: center; padding-top: 4px;
  }
  .event-body { flex: 1; }
  .event:first-of-type .event-body { border-bottom: 1px solid var(--rule); padding-bottom: 18px; }
  .event-title { font-size: 11px; font-weight: 600; text-transform: uppercase; margin-bottom: 6px; }
  .event-text { font-size: 13px; line-height: 17px; }

  .site-footer {
    margin-top: 32px; height: 182px; background: var(--lime); border-radius: 7px;
    position: relative; color: var(--white);
  }
  .copyright { position: absolute; left: 24px; top: 20px; font-size: 13px; }
  .footer-links { position: absolute; left: 27px; top: 60px; color: #111; }
  .footer-links h3 { font-size: 16px; font-weight: 500; margin-bottom: 16px; }
  .footer-links li { list-style: none; font-size: 13.5px; line-height: 19px; }
  .footer-links li::before { content: "»"; margin-right: 6px; }
  .contact { position: absolute; left: 629px; top: 16px; width: 274px; }
  .contact h3 { font-size: 23px; font-weight: 600; margin-bottom: 8px; }
  .contact p { font-size: 13.5px; line-height: 23px; }
  .contact .phone { color: #111; }
  .contact hr { border: none; border-top: 1px solid var(--lime-dark); margin: 13px 0 14px; }
  .newsletter { display: flex; gap: 5px; }
  .newsletter input {
    width: 194px; height: 28px; border: none; border-radius: 4px; padding: 0 10px;
    font: 11px "Asap", Arial, sans-serif; color: #999;
  }
  .newsletter button {
    width: 78px; height: 27px; border: none; border-radius: 4px; background: var(--lime-dark);
    color: var(--white); font: 13px "Asap", Arial, sans-serif;
  }
</style>
</head>
<body>
<div class="page">
  <header class="site-header">
    <div class="brand">LindekloofDirect</div>
    <div class="social" aria-label="Social links">
      <span role="img" aria-label="Social profile"></span>
      <span role="img" aria-label="Social profile"></span>
      <span role="img" aria-label="Social profile"></span>
    </div>
  </header>

  <nav class="main-nav">
    <a class="active" href="#">HOME</a>
    <a href="#">ACCOMMODATION</a>
    <a href="#">PLAY</a>
    <a href="#">CONTACT</a>
  </nav>

  <h1 class="tagline">Your booking agent for..</h1>

  <section class="services">
    <article class="service service--stay">
      <h2 class="service-title">Rest Easy</h2>
      <div class="service-photo" role="img" aria-label="Photo of a guest bedroom with a made bed"></div>
      <p class="service-text">Find the perfect accommodation to suit your specific needs. Click on Rest Easy to view and book our properties online NOW!</p>
    </article>
    <article class="service service--play">
      <h2 class="service-title">Go Explore</h2>
      <div class="service-photo" role="img" aria-label="Photo of a concert crowd under stage lights"></div>
      <p class="service-text">Secure your Playlist! Lindekloof has wonderful excursions, activities, shows and festivals on offer. Click on Go Explore and book it all ONLINE.</p>
    </article>
    <article class="service service--eat">
      <h2 class="service-title">Dine Well</h2>
      <div class="service-photo" role="img" aria-label="Photo of a roast dinner with red wine"></div>
      <p class="service-text">WOW! Book your eating experiance with us. As always Lindekloof has the best on offer to enhance your culinary experience. Click Dine Well!</p>
    </article>
  </section>

  <section class="events">
    <h2>Special events and festivals</h2>
    <div class="event">
      <div class="event-date">01<br>apr</div>
      <div class="event-body">
        <div class="event-title">Olive Festival - April 2014</div>
        <p class="event-text">Sed ut perspiciatis unde omnis iste natus error sit voluptatem accusantium doloremque laudantium, totam rem aperiam, eaque ipsa quae ab illo inventore veritatis et quasi architecto beatae</p>
      </div>
    </div>
    <div class="event">
      <div class="event-date">04<br>sep</div>
      <div class="event-body">
        <div class="event-title">Winter School - August 2014</div>
        <p class="event-text">Sed ut perspiciatis unde omnis iste natus error sit voluptatem accusantium doloremque laudantium, totam rem aperiam, eaque ipsa quae ab illo inventore veritatis et quasi architecto beatae</p>
      </div>
    </div>
  </section>

  <footer class="site-footer">
    <p class="copyright">© copyrights Lindekloof Direct. All rights reserved</p>
    <div class="footer-links">
      <h3>Services</h3>
      <ul>
        <li>Business directory</li>
        <li>Relevant links and websites</li>
        <li>Emergency numbers</li>
      </ul>
    </div>
    <div class="contact">
      <h3>Contact Us</h3>
      <p class="phone">Phone: 1-555-014-2290</p>
      <p>E-mail: info@lindekloofdirect.com</p>
      <hr>
      <form class="newsletter">
        <input type="text" placeholder="Newsletter Sign-up">
        <button type="button">Subcribe</button>
      </form>
    </div>
  </footer>
</div>
</body>
</html>
```